Saltwater In store poster design

We need a poster design that will be hung in aquarium stores, to advertise that they use our natural saltwater.

Must use logo as well as be bright and colourful. We are trying to communicate that the water is natural (so good for your marine tank) as well as clean and safe, so please consider this in your design.

Must say something along the lines of "We use natural ocean water supplied by Reef Ready in our store" as well as "you can purchase natural ocean water here"

Open to all design types and suggestions as we will update the brief if we find one specific style that we prefer.

Target Market(s)

Customers who own marine aquariums

Industry/Entity Type

Store

Requirements
Must have
• Reef ready logo (does not need to have blue background attached, just the oval)

Be eye catching

Have similar phrases to those above

```html
<!DOCTYPE html>
<html lang="en">
<head>
<meta charset="utf-8">
<title>Reef Ready – In-Store Saltwater Poster</title>
<link rel="stylesheet" href="https://fonts.googleapis.com/css2?family=Open+Sans:wght@600;700;800&display=swap">
<style>
  :root {
    --frame: #000000;
    --paper: #ffffff;
    --paper-edge: #d4d6d8;
    --ink: #3a3a3a;
    --ocean: #1ea7e4;
    --ocean-light: #4dbcec;
    --foam: #ffffff;
    --product-light: #eef1f3;
    --product-mid: #c9d3d8;
    --product-dark: #7d858b;
  }
  * { box-sizing: border-box; margin: 0; padding: 0; }
  html, body { width: 852px; height: 1200px; overflow: hidden; background: var(--frame); }
  .canvas {
    position: relative;
    width: 852px;
    height: 1200px;
    background: var(--frame);
    font-family: "Open Sans", Arial, sans-serif;
  }
  .poster {
    position: absolute;
    left: 50px; top: 62px;
    width: 752px; height: 1074px;
    overflow: hidden;
    background: radial-gradient(ellipse 64% 60% at 50% 45%, var(--paper) 72%, var(--paper-edge) 100%);
  }
  .brand {
    position: absolute;
    left: 432px; top: 50px;
    display: flex; align-items: center; gap: 10px;
    color: var(--ocean);
    font-weight: 800;
    font-size: 38px;
    line-height: 1;
    letter-spacing: -0.5px;
  }
  .brand-dot {
    width: 20px; height: 20px;
    border-radius: 50%;
    background: var(--ocean);
  }
  .headline {
    position: absolute;
    left: 74px; top: 146px;
    color: var(--ink);
    font-weight: 700;
    font-size: 25px;
    line-height: 34px;
  }
  .product-photo {
    position: absolute;
    left: 200px; top: 318px;
    width: 440px; height: 456px;
    border-radius: 18px;
    background: linear-gradient(180deg, var(--product-light) 0%, var(--product-mid) 55%, var(--product-dark) 100%);
  }
  .promise {
    position: absolute;
    left: 76px; top: 776px;
    width: 480px;
    color: var(--ocean);
    font-weight: 600;
    font-size: 44px;
    line-height: 53px;
    text-align: center;
  }
  .ocean-band {
    position: absolute;
    left: 0; top: 900px;
    width: 752px; height: 174px;
    background: linear-gradient(180deg, var(--ocean-light) 0%, var(--ocean) 35%, var(--ocean) 100%);
  }
  .call {
    position: absolute;
    left: 0; top: 1018px;
    width: 752px;
    text-align: center;
    color: var(--foam);
    font-weight: 700;
    font-size: 38px;
    line-height: 48px;
  }
</style>
</head>
<body>
<main class="canvas">
  <section class="poster">
    <div class="brand"><span class="brand-dot"></span>Reef Ready</div>

    <h1 class="headline">
      We Use Natural Ocean Water Supplied<br>
      by Reef Ready In Our Store<br>
      As Well As<br>
      You Can Purchase.
    </h1>

    <div class="product-photo" role="img" aria-label="Photo of a small black desktop aquarium with a lamp, fish, plants and pebbles, a pen holder with scissors and a phone, and a digital clock display"></div>

    <p class="promise">It’s good, clean &amp; safe<br>for your Marine tanks</p>

    <div class="ocean-band" role="img" aria-label="Blue ocean wave decoration along the bottom of the poster"></div>

    <p class="call">Call Us: 98-765-4321</p>
  </section>
</main>
</body>
</html>
```